Willowmere Equine Sanctuary Flyer Urgent

Willowmere Equine Sanctuary

Rescue • Rehabilitation • Sanctuary

Willowmere Equine Sanctuary provides a safe and ethical refuge for horses, ponies and donkeys who have nowhere else to go. Some arrive needing rehabilitation and careful retraining, while others find permanent sanctuary here due to age, injury or behavioural needs.

Our mission is simple: to improve the physical and psychological wellbeing of every animal in our care.

At Willowmere we focus on:
• Rescue and rehabilitation of horses in need
• Lifetime sanctuary for those who cannot be rehomed
• Education and advocacy for responsible horse care
• Equine rehabilitation services to help horses recover and thrive

Sponsor a Horse

One of the most meaningful ways to support our work is by sponsoring one of our residents. Each horse, pony or donkey only has one sponsor!

Your sponsorship helps provide:
• Hay and feed
• Veterinary care
• Hoof trimming and routine health care
• Rugs, shelter and daily care

Many of our horses will live out their lives here, and sponsorship ensures they are safe, well fed and cared for every single day.

Sponsorship starts from $15 - $25 per week / $60 -$100 per month.

How You Can Help

• Sponsor a horse
• Make a donation
• Share our work with others

Your support helps us continue to say yes to horses who need a second chance.

📍 Willowmere Park, Victoria
📧 clara@willowmerepark-example.org

📞 0400 519 627

Font styles to use
Serif
Sans Serif

Colors
F0912C
F2A743
F7CA91
FBE8D2
FDF5EE
EE7325
F08F49
F5BC92
FAE3D3
FDF4ED

Requirements
Should not have
• Photos not provided by Willowmere

```html
<!DOCTYPE html>
<html lang="en">
<head>
<meta charset="utf-8">
<title>Willowmere Equine Sanctuary – Sponsorship Flyer</title>
<link href="https://fonts.googleapis.com/css2?family=Poppins:wght@300;400;500;600;700;800&display=swap" rel="stylesheet">
<style>
  :root{
    --orange:#F28A2E;
    --red:#E84D35;
    --ink:#2F2F2F;
    --dark-panel:#333333;
    --white:#FFFFFF;
    --hero-dark:#3E3B2E;
    --frame-line:#F1A294;
  }
  *{margin:0;padding:0;box-sizing:border-box}
  html,body{width:895px;height:1200px;overflow:hidden;background:var(--white)}
  body{font-family:"Poppins",sans-serif;color:var(--ink)}
  .flyer{position:relative;width:895px;height:1200px;background:var(--white)}
  .abs{position:absolute}

  .hero-photo{left:0;top:0;width:895px;height:325px;
    background:linear-gradient(180deg,#4A4B3C 0%,#5B5440 45%,#4E4A39 70%,#6B7150 100%)}
  .hero-shade{left:0;top:0;width:895px;height:325px;background:rgba(30,28,22,.35)}

  .brand{left:52px;top:98px;display:flex;align-items:center;gap:12px}
  .brand-name{color:var(--white);font-weight:500;font-size:30px;line-height:1.05;text-align:right}
  .brand-mark{width:66px;height:118px;background:var(--orange)}

  .title{left:364px;top:70px;font-weight:800;font-size:40px;line-height:51px;letter-spacing:-1.2px;color:var(--white);text-transform:uppercase}
  .title .accent{color:var(--orange)}
  .tagline{left:364px;top:178px;color:var(--white);font-size:23px;font-weight:400;letter-spacing:-.3px}

  .intro-band{left:60px;top:275px;width:776px;height:109px;background:var(--red);color:var(--white);
    font-size:16.5px;line-height:23px;text-align:center;padding:20px 40px 0;letter-spacing:-.3px}

  .mission-head{left:60px;top:412px;color:var(--red);font-size:24px;font-weight:400;letter-spacing:-.4px}
  .mission-body{left:60px;top:449px;width:330px;font-size:18px;line-height:25px;letter-spacing:-.3px}

  .focus-head{left:60px;top:543px;font-size:24px;font-weight:800;line-height:29px;letter-spacing:-.8px;text-transform:uppercase}

  .ticks{list-style:none}
  .ticks li{position:relative;padding-left:24px;font-size:17px;line-height:21px;font-weight:300;letter-spacing:-.1px}
  .ticks svg{position:absolute;left:0;top:3px;width:15px;height:14px}
  .focus-list{left:60px;top:606px;width:330px}
  .focus-list li{margin-bottom:9px}
  .focus-list svg path{stroke:var(--orange)}

  .sponsor-panel{left:34px;top:850px;width:383px;height:170px;background:var(--dark-panel);color:var(--white);padding:20px 26px}
  .sponsor-panel h2{font-size:24px;font-weight:800;letter-spacing:-.8px;line-height:30px;text-transform:uppercase}
  .sponsor-panel p{font-size:16.5px;line-height:23px;letter-spacing:-.4px}

  .contact{left:60px;width:400px;display:flex;align-items:center;gap:12px;font-size:19px;font-weight:300;letter-spacing:-.2px}
  .contact svg{width:18px;height:18px;flex:none}
  .contact.phone{top:1043px;font-size:25px;font-weight:400}
  .contact.pin{top:1080px}
  .contact.mail{top:1110px}

  .sponsorship-frame{left:463px;top:406px;width:373px;height:171px;border:1px solid var(--frame-line)}
  .sponsorship-head{left:478px;top:418px;font-size:26px;font-weight:800;letter-spacing:-.8px;text-transform:uppercase}
  .sponsorship-body{left:478px;top:458px;width:350px;font-size:16.5px;line-height:22px;letter-spacing:-.4px}
  .price{top:544px;width:154px;height:86px;color:var(--white);text-align:center;padding-top:17px;font-weight:600;letter-spacing:-.4px}
  .price b{display:block;font-size:23px;line-height:26px;font-weight:600}
  .price span{font-size:15.5px}
  .price.weekly{left:492px;background:var(--orange)}
  .price.monthly{left:655px;background:var(--red)}

  .supports-head{left:478px;top:658px;color:var(--red);font-size:24px;font-weight:800;line-height:29px;letter-spacing:-.8px;text-transform:uppercase}
  .supports-list{left:478px;top:730px;width:330px}
  .supports-list li{margin-bottom:9px}
  .supports-list svg path{stroke:var(--ink)}

  .help-head{left:478px;top:874px;font-size:24px;font-weight:800;letter-spacing:-.8px;text-transform:uppercase}
  .help-list{left:478px;top:918px;list-style:none}
  .help-list li{display:flex;align-items:center;gap:13px;font-size:19.5px;font-weight:300;height:37px;letter-spacing:-.2px}
  .help-list svg{width:17px;height:18px}

  .closing{left:463px;top:1042px;width:373px;height:113px;background:var(--red);color:var(--white);
    font-size:19.5px;font-weight:600;line-height:28px;letter-spacing:-.6px;padding:14px 16px 0 19px}
</style>
</head>
<body>
<main class="flyer">
  <div class="abs hero-photo" role="img" aria-label="Photo of a herd of horses grazing by a fence in a paddock with gum trees"></div>
  <div class="abs hero-shade"></div>

  <div class="abs brand">
    <div class="brand-name">Willowmere<br>Park</div>
    <div class="brand-mark"></div>
  </div>

  <h1 class="abs title">Willowmere <span class="accent">Equine</span><br><span class="accent">Equine</span> Sanctuary</h1>
  <p class="abs tagline">· Rehabilitation · Sanctuary · Rescue</p>

  <p class="abs intro-band">We provide a safe, ethical refuge for horses, ponies, and donkeys. Some arrive needing rehabilitation, while others find lifelong sanctuary due to age, injury, or behavioral needs.</p>

  <h2 class="abs mission-head">Our mission is simple</h2>
  <p class="abs mission-body">to improve the physical and psychological wellbeing of every animal in our care.</p>

  <h2 class="abs focus-head">At Willowmere,<br>we focus on</h2>
  <ul class="abs ticks focus-list">
    <li><svg viewBox="0 0 15 14"><path d="M1.5 7.5l4 4L13.5 2" fill="none" stroke-width="2.2" stroke-linecap="round" stroke-linejoin="round"/></svg>Rescuing and rehabilitating horses in need</li>
    <li><svg viewBox="0 0 15 14"><path d="M1.5 7.5l4 4L13.5 2" fill="none" stroke-width="2.2" stroke-linecap="round" stroke-linejoin="round"/></svg>Providing lifelong sanctuary for horses that cannot be rehomed</li>
    <li><svg viewBox="0 0 15 14"><path d="M1.5 7.5l4 4L13.5 2" fill="none" stroke-width="2.2" stroke-linecap="round" stroke-linejoin="round"/></svg>Promoting responsible horse care through education &amp; advocacy</li>
    <li><svg viewBox="0 0 15 14"><path d="M1.5 7.5l4 4L13.5 2" fill="none" stroke-width="2.2" stroke-linecap="round" stroke-linejoin="round"/></svg>Supporting equine recovery &amp; wellbeing through rehabilitation services</li>
  </ul>

  <section class="abs sponsor-panel">
    <h2>Sponsor a horse</h2>
    <p>One of the most meaningful ways to support our work is by sponsoring one of our residents. Each horse, pony or donkey only has one sponsor!</p>
  </section>

  <div class="abs contact phone">
    <svg viewBox="0 0 24 24"><path fill="#2F2F2F" d="M6.6 10.8a15.1 15.1 0 006.6 6.6l2.2-2.2a1 1 0 011-.25 11.4 11.4 0 003.6.57 1 1 0 011 1V20a1 1 0 01-1 1A17 17 0 013 4a1 1 0 011-1h3.5a1 1 0 011 1c0 1.25.2 2.45.57 3.57a1 1 0 01-.25 1z"/></svg>
    0400 519 627
  </div>
  <div class="abs contact pin">
    <svg viewBox="0 0 24 24"><path fill="#2F2F2F" d="M12 2a7 7 0 00-7 7c0 5.2 7 13 7 13s7-7.8 7-13a7 7 0 00-7-7zm0 9.5A2.5 2.5 0 1112 6.5a2.5 2.5 0 010 5z"/></svg>
    Willowmere Park, Victoria
  </div>
  <div class="abs contact mail">
    <svg viewBox="0 0 24 24"><path fill="#2F2F2F" d="M3 6h18v12H3z"/><path d="M3 6.5l9 6 9-6" fill="none" stroke="#fff" stroke-width="1.6"/></svg>
    clara@willowmerepark-example.org
  </div>

  <div class="abs sponsorship-frame"></div>
  <h2 class="abs sponsorship-head">Sponsorship</h2>
  <p class="abs sponsorship-body">Many of our horses will spend their lives here, &amp; sponsorship ensures they are safe, well-fed, &amp; cared for daily.</p>
  <div class="abs price weekly"><b>$15–$25</b><span>per week</span></div>
  <div class="abs price monthly"><b>$60–$100</b><span>per month</span></div>

  <h2 class="abs supports-head">Your sponsorship<br>supports</h2>
  <ul class="abs ticks supports-list">
    <li><svg viewBox="0 0 15 14"><path d="M1.5 7.5l4 4L13.5 2" fill="none" stroke-width="2.2" stroke-linecap="round" stroke-linejoin="round"/></svg>Hay, nutritious feed &amp; Veterinary care</li>
    <li><svg viewBox="0 0 15 14"><path d="M1.5 7.5l4 4L13.5 2" fill="none" stroke-width="2.2" stroke-linecap="round" stroke-linejoin="round"/></svg>Hoof trimming and routine health maintenance</li>
    <li><svg viewBox="0 0 15 14"><path d="M1.5 7.5l4 4L13.5 2" fill="none" stroke-width="2.2" stroke-linecap="round" stroke-linejoin="round"/></svg>Shelter, rugs, and daily care</li>
  </ul>

  <h2 class="abs help-head">How you can help</h2>
  <ul class="abs help-list">
    <li><svg viewBox="0 0 17 18"><path d="M3 2v7a5.5 5.5 0 0011 0V2" fill="none" stroke="#E84D35" stroke-width="3.4"/></svg>Sponsor a horse</li>
    <li><svg viewBox="0 0 17 18"><path d="M3 2v7a5.5 5.5 0 0011 0V2" fill="none" stroke="#E84D35" stroke-width="3.4"/></svg>Make a donation</li>
    <li><svg viewBox="0 0 17 18"><path d="M3 2v7a5.5 5.5 0 0011 0V2" fill="none" stroke="#E84D35" stroke-width="3.4"/></svg>Share our work with others</li>
  </ul>

  <p class="abs closing">Your support helps us continue to say yes to horses who need a second chance.</p>
</main>
</body>
</html>
```